Business card design needed

I run a Beautician studio (for 7 years now)
I offer
- Vestolin Body Sugaring
- Velumi Glow
- Nails
- Facials
- Manicure
- Foot Treatment
It might not be necessary to list all those treatments?
Maybe the link to the Website is sufficient?
I leave that up to you ...
(more info on www.BuffsAndBrowsByMarisol.com.au)
Vestolin BodySugaring is our biggest success, It replaces waxing.
I would like to incorporate the logo into the Business Card.
We had many complaints regarding our old Business Cards as the Phone Number was to small.
On the backside, we would like a "your next Appointment" section.
Looking forward to you Design, cheers ... Marisol
Buffs by Brows by Marisol
14 Merindo Cct 3912 Berwick
www.BuffsAndBrowsByMarisol.com.au
03 9418 2276

```html
<!DOCTYPE html>
<html lang="en">
<head>
<meta charset="utf-8">
<title>Buffs by Brows by Marisol – Business Cards</title>
<link rel="stylesheet" href="https://fonts.googleapis.com/css2?family=Arimo:wght@400;700&family=Cinzel:wght@500&family=Open+Sans:wght@400;600;700&display=swap">
<style>
  :root {
    --backdrop: #1c1c1c;
    --card: #ffffff;
    --green: #1f9a45;
    --ink: #1a1a1a;
    --grey: #555555;
    --rule: #7a7a7a;
  }
  * { box-sizing: border-box; margin: 0; padding: 0; }
  html, body { width: 1200px; height: 728px; overflow: hidden; }
  body { background: var(--backdrop); position: relative; font-family: "Open Sans", Arial, sans-serif; color: var(--ink); }

  .card { position: absolute; width: 541px; height: 307px; background: var(--card); overflow: hidden; }
  .card--front { left: 42px; top: 38px; }
  .card--appointment-a { left: 616px; top: 38px; }
  .card--hours { left: 44px; top: 381px; height: 308px; }
  .card--appointment-b { left: 625px; top: 385px; }

  /* brand name stand-in: plain text in the piece's own text font */
  .brand { position: absolute; font-family: "Open Sans", Arial, sans-serif; font-weight: 600; color: var(--ink); text-align: center; line-height: 1.2; }
  .card--front .brand { left: 350px; top: 218px; width: 170px; font-size: 20px; }
  .card--appointment-a .brand { left: 380px; top: 40px; width: 120px; font-size: 14px; }
  .card--hours .brand { left: 0; right: 0; top: 112px; font-size: 32px; letter-spacing: .5px; }

  /* front */
  .front { padding: 36px 0 0 30px; font-family: "Arimo", Arial, sans-serif; }
  .front__title { font-size: 21px; font-weight: 700; color: var(--green); letter-spacing: .3px; }
  .front__address { font-size: 14px; margin-top: 3px; }
  .contact { display: flex; align-items: center; gap: 8px; }
  .contact--phone { font-size: 16.5px; margin-top: 20px; }
  .contact--web { font-size: 14px; margin-top: 9px; }
  .contact svg { flex: none; }
  .front__heading { font-size: 16.5px; font-weight: 700; color: var(--green); letter-spacing: 1px; margin-top: 24px; }
  .treatments { list-style: none; font-size: 14.5px; line-height: 21.5px; margin-top: 3px; }

  /* appointment */
  .appt { padding: 52px 0 0 36px; font-size: 15px; color: #333; }
  .appt__title { font-family: "Cinzel", Georgia, serif; font-weight: 500; color: var(--green); font-size: 18px; letter-spacing: .3px; }
  .row { display: flex; align-items: flex-end; margin-top: 16px; height: 22px; }
  .row:first-of-type { margin-top: 8px; }
  .fill { display: inline-block; border-bottom: 1px solid var(--rule); height: 1px; margin: 0 6px 6px; }
  .fill--dotted { border-bottom: 1px dotted var(--rule); }
  .box { display: inline-block; width: 98px; height: 22px; border: 1px solid #444; margin-left: 10px; }
  .days { display: flex; align-items: center; margin-top: 16px; font-weight: 600; color: #555; font-size: 15px; }
  .days .day { margin-right: 8px; }
  .days .tick { width: 34px; height: 21px; border: 1px solid #444; margin-right: 8px; }
  .appt__note { font-size: 13px; line-height: 17px; margin-top: 26px; width: 470px; color: #333; }

  /* hours */
  .hours { position: absolute; left: 0; right: 0; top: 200px; text-align: center; color: var(--grey); }
  .hours__web { font-size: 14px; letter-spacing: 2px; color: var(--ink); }
  .hours__title { font-size: 20px; font-weight: 600; letter-spacing: 1.5px; margin-top: 14px; }
  .hours__times { font-size: 15px; font-weight: 600; margin-top: 10px; }
  .hours__sep { color: #999; padding: 0 6px; font-weight: 400; }
</style>
</head>
<body>

<section class="card card--front">
  <div class="front">
    <h1 class="front__title">Buffs by Brows by Marisol</h1>
    <p class="front__address">14 Merindo Cct 3912 Berwick</p>
    <p class="contact contact--phone">
      <svg width="14" height="14" viewBox="0 0 24 24" aria-hidden="true"><path d="M6.6 10.8a15 15 0 0 0 6.6 6.6l2.2-2.2c.3-.3.7-.4 1-.2 1.1.4 2.3.6 3.6.6.6 0 1 .4 1 1V20c0 .6-.4 1-1 1C10.6 21 3 13.4 3 4c0-.6.4-1 1-1h3.5c.6 0 1 .4 1 1 0 1.3.2 2.5.6 3.6.1.3 0 .7-.2 1z" fill="#222"/></svg>
      03 9418 2276
    </p>
    <p class="contact contact--web">
      <svg width="13" height="13" viewBox="0 0 24 24" aria-hidden="true"><circle cx="12" cy="12" r="10" fill="none" stroke="#1f9a45" stroke-width="2"/><ellipse cx="12" cy="12" rx="4.5" ry="10" fill="none" stroke="#1f9a45" stroke-width="2"/><path d="M2 12h20M4 7h16M4 17h16" stroke="#1f9a45" stroke-width="1.6"/></svg>
      www.BuffsAndBrowsByMarisol.com.au
    </p>
    <h2 class="front__heading">Treatments offer</h2>
    <ul class="treatments">
      <li>• Vestolin Body Sugaring</li>
      <li>• Velumi Glow • Nails</li>
      <li>• Facials • Manicure</li>
      <li>• Foot Treatment</li>
    </ul>
  </div>
  <p class="brand">Vestolin Body Sugaring</p>
</section>

<section class="card card--appointment-a">
  <div class="appt">
    <h2 class="appt__title">YOUR APPOINTMENT</h2>
    <div class="row">Name :<span class="fill fill--dotted" style="width:290px"></span></div>
    <div class="row">Date :<span class="fill" style="width:96px;margin-left:22px"></span>Time :<span class="fill" style="width:90px"></span>am / pm</div>
    <div class="row">Next Appointment<span class="box"></span><span class="box" style="margin-left:28px"></span></div>
    <div class="days">
      <span class="day">MON</span><span class="tick"></span><span class="day">TUE</span><span class="tick"></span><span class="day">WED</span><span class="tick"></span><span class="day">THU</span><span class="tick"></span><span class="day">FRI</span><span class="tick"></span><span class="day">SAT</span><span class="tick"></span>
    </div>
    <p class="appt__note">It would be appreciated if 24 hours notice could be given if you are unable to attend an appointment</p>
  </div>
  <p class="brand">Vestolin Body Sugaring</p>
</section>

<section class="card card--hours">
  <p class="brand">Vestolin Body Sugaring</p>
  <div class="hours">
    <p class="hours__web">www.BuffsAndBrowsByMarisol.com.au</p>
    <h2 class="hours__title">Hours of Operation</h2>
    <p class="hours__times">Mon - Fri: 7.30am - 7.00pm <span class="hours__sep">|</span> Saturday: 7.30am - 12.00pm</p>
  </div>
</section>

<section class="card card--appointment-b">
  <div class="appt">
    <h2 class="appt__title">YOUR APPOINTMENT</h2>
    <div class="row">Name :<span class="fill fill--dotted" style="width:290px"></span></div>
    <div class="row">Date :<span class="fill" style="width:96px;margin-left:22px"></span>Time :<span class="fill" style="width:90px"></span>am / pm</div>
    <div class="row">Next Appointment<span class="box"></span><span class="box" style="margin-left:28px"></span></div>
    <div class="days">
      <span class="day">MON</span><span class="tick"></span><span class="day">TUE</span><span class="tick"></span><span class="day">WED</span><span class="tick"></span><span class="day">THU</span><span class="tick"></span><span class="day">FRI</span><span class="tick"></span><span class="day">SAT</span><span class="tick"></span>
    </div>
    <p class="appt__note">It would be appreciated if 24 hours notice could be given if you are unable to attend an appointment</p>
  </div>
</section>

</body>
</html>
```